Redesign my business cards

I would like pretty much all the same information as my current business cards but redesigned to stand out more and be more unique photo uploaded to show my current business cards don’t mind if you want to remove or replace I for on the back

```html
<!DOCTYPE html>
<html lang="en">
<head>
<meta charset="utf-8">
<title>Velmora Detailing – Business Cards</title>
<link rel="stylesheet" href="https://fonts.googleapis.com/css2?family=Lato:wght@400;700&display=swap">
<style>
:root{
  --bg:#d3d3d3;
  --card-front:#ececec;
  --card-back:#23286a;
  --brand-blue:#1b6b96;
  --text-grey:#5a5a5a;
  --accent-pink:#c0489d;
  --price-pink:#b44594;
  --back-text:#eef0f8;
  --art-violet:#6a4aa6;
  --art-blue:#2f6fc0;
  --art-cyan:#3fb4d8;
}
*{margin:0;padding:0;box-sizing:border-box}
html,body{width:1200px;height:706px;overflow:hidden}
body{background:var(--bg);font-family:"Lato",sans-serif;position:relative}
.card{position:absolute;top:169px;width:479px;height:269px;border-radius:24px;overflow:hidden}
.card--front{left:86px;background:linear-gradient(180deg,#f1f1f1,#e3e3e3)}
.card--back{left:644px;background:var(--card-back)}

.brand{position:absolute;left:46px;top:62px;display:flex;align-items:center;gap:8px}
.brand__dot{width:14px;height:14px;border-radius:50%;background:var(--brand-blue)}
.brand__name{font-weight:700;font-size:13px;letter-spacing:.5px;color:var(--brand-blue)}

.owner{position:absolute;left:46px;top:163px}
.owner__name{font-weight:700;font-size:15.5px;color:var(--brand-blue);letter-spacing:.2px}
.owner__role{font-size:11px;color:var(--text-grey);margin-top:2px}
.contact{position:absolute;left:46px;top:207px;font-size:11px;color:var(--text-grey);line-height:14px}
.contact__row{display:flex;align-items:center;gap:6px}
.contact__row svg{width:9px;height:9px;fill:var(--brand-blue)}

.art{position:absolute;border-radius:46% 0 0 50%/50% 0 0 50%}
.art--front{right:0;top:0;width:131px;height:254px;background:linear-gradient(160deg,var(--art-blue),var(--art-violet) 55%,var(--art-cyan))}
.art--back{left:0;top:10px;width:130px;height:259px;border-radius:0 48% 50% 0/0 50% 50% 0;background:linear-gradient(160deg,#c9b7de,#8fb6e0 55%,#4f7fd0)}

.price{position:absolute;left:141px;font-weight:700;font-size:21px;color:var(--price-pink)}
.service{position:absolute;left:209px;width:232px}
.service__title{font-weight:700;font-size:13px;color:var(--accent-pink);line-height:15px}
.service__text{font-size:10.8px;color:var(--back-text);line-height:13px}
</style>
</head>
<body>
<section class="card card--front">
  <div class="brand"><span class="brand__dot"></span><span class="brand__name">VELMORA DETAILING</span></div>
  <div class="owner">
    <div class="owner__name">DANE WHITLOW</div>
    <div class="owner__role">Owner/Operator</div>
  </div>
  <div class="contact">
    <div class="contact__row"><svg viewBox="0 0 10 10"><path d="M2 0.5l1.6 0 .7 2.3-1 .8c.6 1.3 1.6 2.3 2.9 2.9l.8-1 2.3.7 0 1.6c0 .6-.5 1.2-1.2 1.2C4 8.8 1.2 6 .8 1.7.8 1 1.3.5 2 .5z"/></svg>0400512774</div>
    <div class="contact__row"><svg viewBox="0 0 10 10"><path d="M0 2h10v6H0z M0 2l5 3.5L10 2" fill="var(--brand-blue)"/><path d="M0 2l5 3.5L10 2" stroke="#fff" stroke-width=".8" fill="none"/></svg>velmoradetailing@mailbox.com</div>
  </div>
  <div class="art art--front" role="img" aria-label="Illustration of a car front surrounded by a water splash"></div>
</section>

<section class="card card--back">
  <div class="art art--back" role="img" aria-label="Illustration of a car front surrounded by a water splash"></div>
  <div class="price" style="top:38px">$150</div>
  <div class="price" style="top:100px">$250</div>
  <div class="price" style="top:183px">$350</div>
  <div class="service" style="top:24px">
    <div class="service__title">INTERIOR DETAIL</div>
    <p class="service__text">Vacume &amp; deep clean of carpets&nbsp; upholstery or leather treatment, interiro trim clean condition. Windows polish and treatment, steam clean and stain removal.</p>
  </div>
  <div class="service" style="top:99px">
    <div class="service__title">EXTERIOR DETAIL</div>
    <p class="service__text">Extreme wash &amp; polish, exterior trim reviver &amp; protector windows. Polish &amp; treatment, tyre dressing, engine bay cleaned</p>
  </div>
  <div class="service" style="top:161px">
    <div class="service__title">FULL EXTREMEDETAIL</div>
    <p class="service__text">Extreme wash &amp; polish, tyre dressing, engine bay cleaned, vacume &amp; deep clean of carpets upholstery or leather treatment, interior &amp; exterior trim reviver &amp; protector, window polish and treatment</p>
  </div>
</section>
</body>
</html>
```